Wine label refresh

We are wanting to modify our Corran Hollow label to include a picture on it.
I have attached the pictures below which we would like on the label. They are of the Corran Hollow vineyard. I have also attached an example of another label with a picture on it that we like the style of.
Updates
Industry/Entity Type
Vineyard
Requirements
Must have
- The Corran Hollow text must stay the same but can be moved down. It still needs to be the same size though.
Marlborough Sauvignon Blanc should remain in the same font and roughly the same size.
Wine of New Zealand also must stay but could potentially be moved.
Nice to have
- It would be nice if we could keep the PM logo on the front label but feel free to experiment with where this goes.

```html
<!DOCTYPE html>
<html lang="en">
<head>
<meta charset="utf-8">
<title>Corran Hollow – Marlborough Sauvignon Blanc 2012</title>
<link href="https://fonts.googleapis.com/css2?family=Cormorant+Garamond:wght@500;600&family=Pinyon+Script&family=Lato:wght@300&display=swap" rel="stylesheet">
<style>
  :root {
    --sky-top: #7c7d79;
    --sky-mid: #c9cac6;
    --sky-low: #e6e6e2;
    --gold-light: #f1d9a9;
    --gold-mid: #dcb975;
    --gold-deep: #b48a36;
    --accent-red: #c8203c;
    --ink: #1b1a17;
    --frame: #000000;
    --photo-tone: #8a9478;
    --photo-tone-soft: #9ca38e;
    --white: #ffffff;
  }
  html, body {
    margin: 0;
    padding: 0;
    width: 1200px;
    height: 898px;
    overflow: hidden;
    background: #ffffff;
  }
  .label {
    position: relative;
    width: 1200px;
    height: 898px;
    overflow: hidden;
    background: linear-gradient(to bottom, var(--sky-top) 0px, var(--sky-mid) 120px, var(--sky-low) 300px, var(--sky-low) 550px);
  }
  .label__band {
    position: absolute;
    left: 0;
    top: 550px;
    width: 1200px;
    height: 348px;
    background: linear-gradient(to bottom, var(--gold-light) 0%, var(--gold-light) 18%, var(--gold-mid) 55%, var(--gold-deep) 100%);
  }
  .rule {
    position: absolute;
    top: 90px;
    height: 3px;
    background: var(--accent-red);
  }
  .rule--left { left: 44px; width: 382px; }
  .rule--right { left: 774px; width: 382px; }
  .monogram {
    position: absolute;
    left: 0;
    top: 14px;
    width: 1200px;
    text-align: center;
    font-family: "Cormorant Garamond", serif;
    font-weight: 600;
    font-size: 130px;
    line-height: 1;
    letter-spacing: 4px;
    color: var(--ink);
  }
  .vineyard-photo {
    position: absolute;
    left: 260px;
    top: 184px;
    width: 666px;
    height: 344px;
    border: 6px solid var(--frame);
    background: linear-gradient(to bottom, var(--photo-tone-soft), var(--photo-tone));
  }
  .estate-name {
    position: absolute;
    left: 0;
    top: 567px;
    width: 1200px;
    margin: 0;
    text-align: center;
    font-family: "Cormorant Garamond", serif;
    font-weight: 500;
    font-size: 88px;
    font-variant: small-caps;
    letter-spacing: 3px;
    line-height: 1;
    color: var(--accent-red);
  }
  .varietal {
    position: absolute;
    left: 0;
    top: 688px;
    width: 1200px;
    margin: 0;
    text-align: center;
    font-family: "Pinyon Script", cursive;
    font-weight: 400;
    font-size: 75px;
    line-height: 1;
    color: var(--ink);
  }
  .vintage {
    position: absolute;
    left: 0;
    top: 758px;
    width: 1200px;
    text-align: center;
    font-family: "Pinyon Script", cursive;
    font-size: 56px;
    line-height: 1;
    color: var(--ink);
  }
  .origin {
    position: absolute;
    left: 0;
    top: 826px;
    width: 1200px;
    text-align: center;
    font-family: "Lato", sans-serif;
    font-weight: 300;
    font-size: 49px;
    letter-spacing: 2px;
    line-height: 1;
    color: var(--white);
  }
</style>
</head>
<body>
  <main class="label">
    <div class="label__band"></div>
    <div class="rule rule--left"></div>
    <div class="rule rule--right"></div>
    <div class="monogram">PM</div>
    <div class="vineyard-photo" role="img" aria-label="Photograph of the Corran Hollow vineyard with vines, palm trees and hills"></div>
    <h1 class="estate-name">Corran Hollow</h1>
    <p class="varietal">Marlborough Sauvignon Blanc</p>
    <div class="vintage">2012</div>
    <div class="origin">WINE OF NEW ZEALAND</div>
  </main>
</body>
</html>
```